Business Card Design

Business card design.

Business card is to have logo, website address and email address.

Website is www.brightkettle.ie
Email is info@brightkettle.ie
Logo uploaded

I have ordered Business Card Printing via Print Harbor, the Double-sided colour printed option with gloss finish.

Industry/Entity Type

Business

```html
<!DOCTYPE html>
<html lang="en">
<head>
<meta charset="utf-8">
<title>Bright Kettle – Business Card</title>
<link rel="stylesheet" href="https://fonts.googleapis.com/css2?family=Arimo:wght@700&display=swap">
<style>
  :root {
    --page: #ffffff;
    --card: #0a0b0b;
    --brand-red: #d4101a;
    --brand-red-deep: #8e0a12;
    --ink-light: #ffffff;
    --outline: #e8e8e8;
  }
  html, body {
    margin: 0;
    padding: 0;
    width: 894px;
    height: 1200px;
    overflow: hidden;
    background: var(--page);
  }
  .sheet {
    position: relative;
    width: 894px;
    height: 1200px;
    font-family: "Arimo", Arial, sans-serif;
    font-weight: 700;
  }
  .card {
    position: absolute;
    left: 40px;
    width: 813px;
    height: 527px;
    background: var(--card);
  }
  .card--front { top: 45px; }
  .card--back  { top: 628px; }

  /* Brand lockup: plain circle + name */
  .brand {
    position: absolute;
    display: flex;
    align-items: center;
    color: var(--ink-light);
    white-space: nowrap;
  }
  .brand__dot {
    border-radius: 50%;
    background: var(--brand-red);
    flex: none;
  }
  .brand--hero {
    left: 0;
    right: 0;
    top: 158px;
    flex-direction: column;
    gap: 20px;
  }
  .brand--hero .brand__dot { width: 98px; height: 98px; }
  .brand--hero .brand__name { font-size: 56px; letter-spacing: -0.5px; line-height: 1; }

  .brand--small {
    left: 35px;
    top: 40px;
    gap: 10px;
  }
  .brand--small .brand__dot { width: 30px; height: 30px; }
  .brand--small .brand__name { font-size: 19px; line-height: 1; }

  /* Contact block */
  .contact {
    position: absolute;
    right: 26px;
    top: 330px;
    display: grid;
    grid-template-columns: auto auto;
    column-gap: 28px;
    row-gap: 12px;
    font-size: 56px;
    line-height: 1.05;
    letter-spacing: 0.5px;
  }
  .contact__label {
    text-align: right;
    color: var(--card);
    -webkit-text-stroke: 2px var(--outline);
  }
  .contact__value {
    color: var(--brand-red);
    background: linear-gradient(180deg, var(--brand-red) 0%, var(--brand-red) 45%, var(--brand-red-deep) 100%);
    -webkit-background-clip: text;
    background-clip: text;
    -webkit-text-fill-color: transparent;
    -webkit-text-stroke: 1.5px var(--outline);
  }
</style>
</head>
<body>
<main class="sheet">
  <section class="card card--front" aria-label="Card front">
    <div class="brand brand--hero">
      <span class="brand__dot"></span>
      <span class="brand__name">BRIGHTKETTLE.IE</span>
    </div>
  </section>

  <section class="card card--back" aria-label="Card back">
    <div class="brand brand--small">
      <span class="brand__dot"></span>
      <span class="brand__name">BRIGHTKETTLE.IE</span>
    </div>
    <div class="contact">
      <span class="contact__label">web:</span>
      <span class="contact__value">www.brightkettle.ie</span>
      <span class="contact__label">email:</span>
      <span class="contact__value">info@brightkettle.ie</span>
    </div>
  </section>
</main>
</body>
</html>
```